Poster Design for company teaching children how to cook

Bright Pantry is a local business providing 2 key services (and 1 lesser):
1. After School Cookery clubs
2. Parties
(3. Cookery Classes for pre-schoolers)
A good summary can be found at our website www.bright-pantry.co.uk
We want a poster that we can display at various events, for example, outside parties, alongside demonstrations and in schools. We also would like to replicate the design for advertisement use in press.
We want to communicate that our classes and parties are good fun whilst at the same time being great for children's confidence and skills.
Please contact me tom@bright-pantry.co.uk with any questions and for company logo files.

Now I have sorted out the wording as follows, thanks for your patience:

inspiring children to cook (n.b. lower case as is the wording in the logo)

Classes

- Create nutritious food from scratch that can be replicated at home

- Increase confidence and skills in the kitchen

- Promote awareness of the importance of a nutritionally balanced diet

Parties

- Let us take the stress and run the party for you by providing the entertainment at the same time as the catering

- A variety of sweet and savoury dishes to choose from

- Party bags and invitations included

Call Morwenna now on 07519 620387 for more information or visit www.bright-pantry.co.uk

Since the call to action now contains contact details these need not be repeated elsewhere

Target Market(s)

Children at our classes are generally in the primary school age group 6-11 year olds although our parties reach a slightly wider group 4-13.
We obviously look to appeal to this group directly but also appealing to their parents, the budget holders, should not be underestimated!

Requirements
Must have
• A strong image (please pick from attachments)
• Company logo
• Company contact details including website, email address and phone
• Strapline / Call to action (Wording to be confirmed)
• Two textual areas where we can describe the benefits from parties/classes (about 40-50 words maximum in each. Wording to be confirmed)
• Any use of colour needs to be consistent with the logo palette
• colours are CMYK - Navy & Caribbean Blue
• green - CMYK Mint Julep
• purple - CMYK Amethyst
• Blue - CMYK Caribbean Blue
• Purple light
• C 0
• M 100
• Y 0
• K 0
• Purple dark
• C 50
• M 100
• Y 0
• K 0
• Green light
• C 50
• M 0
• Y 100
• K 0
• Green dark
• C 75
• M 0
• Y 100
• K 25
• Blue light
• C 100
• M 0
• Y 0
• K 0
• Blue dark
• C 100
• M 50
• Y 0
• K 0
• Font in Logo is "Brasserie". Any other font used should be unfussy and clear.
Nice to have
• Subject to space and design, maybe a testimonial or two (Wording to be confirmed)
Should not have
• The image should dominate, not the company logo
• No cartoony illustrations

```html
<!DOCTYPE html>
<html lang="en">
<head>
<meta charset="utf-8">
<title>Bright Pantry – inspiring children to cook</title>
<link rel="stylesheet" href="https://fonts.googleapis.com/css2?family=Belleza&family=Delius&family=Short+Stack&display=swap">
<style>
  :root {
    --purple: #7b2c6a;
    --teal: #9de0de;
    --teal-text: #a9e8e4;
    --navy: #1f2f5e;
    --white: #ffffff;
    --photo-dark: #6a4a3a;
    --photo-skin: #e2b4a2;
    --photo-bread: #d9ccb6;
  }
  * { margin: 0; padding: 0; box-sizing: border-box; }
  html, body { width: 800px; height: 1200px; overflow: hidden; background: var(--white); }
  .poster { position: relative; width: 800px; height: 1200px; overflow: hidden; background: var(--white); }

  .hero-photo {
    position: absolute; left: 0; top: 0; width: 800px; height: 730px;
    background:
      radial-gradient(ellipse 260px 160px at 330px 390px, var(--photo-bread) 0%, rgba(217,204,182,0) 100%),
      radial-gradient(ellipse 380px 220px at 560px 250px, var(--photo-skin) 0%, rgba(226,180,162,0) 100%),
      radial-gradient(ellipse 420px 180px at 420px 520px, #e6bfae 0%, rgba(230,191,174,0) 100%),
      linear-gradient(135deg, var(--photo-dark) 0%, #a77e68 40%, #c79d85 70%, #8a6a55 100%);
  }

  .waves { position: absolute; left: 0; top: 0; width: 800px; height: 1200px; }

  .strapline-echo, .strapline {
    position: absolute; font-family: "Short Stack", "Delius", cursive; white-space: nowrap;
    transform-origin: left bottom;
  }
  .strapline-echo {
    left: 24px; top: 498px; font-size: 46px; letter-spacing: 3px;
    color: rgba(255,255,255,0.22); transform: rotate(-5deg);
  }
  .strapline {
    left: 120px; top: 556px; font-size: 34px; letter-spacing: 2px;
    color: var(--white); transform: rotate(-5.5deg);
  }

  .service { position: absolute; top: 676px; width: 295px; color: var(--white); }
  .service--classes { left: 112px; }
  .service--parties { left: 444px; }
  .service-title {
    font-family: "Delius", cursive; font-weight: 400; font-size: 26px;
    color: var(--teal-text); margin-bottom: 22px; line-height: 1.1;
  }
  .service-points { list-style: none; }
  .service-points li {
    font-family: "Belleza", sans-serif; font-size: 15.5px; line-height: 22px;
    margin-bottom: 9px;
  }

  .call-to-action {
    position: absolute; left: 111px; top: 927px;
    font-family: "Belleza", sans-serif; font-size: 15.5px; color: var(--teal-text);
    white-space: nowrap;
  }

  .brand { position: absolute; left: 62px; top: 1128px; display: flex; align-items: center; gap: 10px; }
  .brand-dot { width: 22px; height: 22px; border-radius: 50%; background: var(--purple); }
  .brand-name { font-family: "Delius", cursive; font-size: 30px; color: var(--navy); }

  .contact {
    position: absolute; left: 320px; top: 1113px; width: 400px; text-align: center;
    font-family: "Delius", cursive; font-size: 19px; line-height: 29px; color: var(--navy);
  }
</style>
</head>
<body>
<div class="poster">
  <div class="hero-photo" role="img" aria-label="Close-up photograph of a child's hands pressing a metal cookie cutter into a slice of white bread"></div>

  <svg class="waves" viewBox="0 0 800 1200" aria-hidden="true">
    <path class="wave-purple" fill="var(--purple)"
          d="M0 704 C 250 620, 560 585, 800 636 L800 1040 C 600 1032, 260 1002, 0 950 Z"/>
    <path class="wave-teal" fill="var(--teal)"
          d="M0 982 C 300 1030, 600 1046, 800 1036 L800 1044 C 560 1070, 260 1078, 0 1046 Z"/>
  </svg>

  <div class="strapline-echo" aria-hidden="true">inspiring children to cook</div>
  <h1 class="strapline">inspiring children to cook</h1>

  <section class="service service--classes">
    <h2 class="service-title">Classes</h2>
    <ul class="service-points">
      <li>Create nutritious food from scratch that can be replicated at home</li>
      <li>Increase confidence and skills in the kitchen</li>
      <li>Promote awareness of the importance of a nutritionally balanced diet</li>
    </ul>
  </section>

  <section class="service service--parties">
    <h2 class="service-title">Parties</h2>
    <ul class="service-points">
      <li>Let us take the stress and run the party for you by providing the entertainment at the same time as the catering</li>
      <li>A variety of sweet and savoury dishes to choose from</li>
      <li>Party bags and invitations included</li>
    </ul>
  </section>

  <p class="call-to-action">Call Morwenna now on 07519 620387 for more information or visit www.bright-pantry.co.uk</p>

  <div class="brand">
    <span class="brand-dot"></span>
    <span class="brand-name">Bright Pantry</span>
  </div>

  <p class="contact">www.bright-pantry.co.uk, tom@bright-pantry.co.uk<br>tel. 07519 620387</p>
</div>
</body>
</html>
```